A label for a gin called Lemon Velvet Meadow Gin

We have attached a mood board below of images that reflect how we would like the label to feel. The words "Lemon Velvet Meadow Gin" are the only important bits that need to be clearly visible.

Font styles to use
Decorative

Colors
eda3c7
e667a6
b768aa
d2a4cc

```html
<!DOCTYPE html>
<html lang="en">
<head>
<meta charset="utf-8">
<title>Lemon Velvet Meadow Gin – Label</title>
<link href="https://fonts.googleapis.com/css2?family=Rye&family=Alfa+Slab+One&display=swap" rel="stylesheet">
<style>
  :root {
    --page: #ffffff;
    --cream: #f6ebe4;
    --blush: #eda3c7;
    --rose: #e667a6;
    --orchid: #b768aa;
    --lilac: #d2a4cc;
    --plum: #7e2c6c;
    --sign-gold: #f0c24f;
    --sign-gold-deep: #d99a2b;
    --sign-paper: #fbf1e6;
    --ink: #2a1a26;
  }
  html, body {
    margin: 0;
    padding: 0;
    width: 1200px;
    height: 1028px;
    overflow: hidden;
    background: var(--page);
  }
  .canvas {
    position: relative;
    width: 1200px;
    height: 1028px;
  }
  .label {
    position: absolute;
    left: 250px;
    top: 104px;
    width: 700px;
    height: 820px;
    background: var(--cream);
    overflow: hidden;
  }
  .sunburst {
    position: absolute;
    inset: 0;
    background: radial-gradient(circle at 50% 42%, var(--cream) 0%, var(--cream) 26%, var(--blush) 58%, var(--rose) 85%, var(--orchid) 100%);
  }
  .bunting {
    position: absolute;
    left: 0;
    top: 160px;
    width: 700px;
    height: 40px;
    background: linear-gradient(90deg, var(--rose), var(--sign-gold), var(--lilac), var(--orchid), var(--rose));
    opacity: 0.8;
  }
  .sign {
    position: absolute;
    left: 62px;
    top: 72px;
    width: 576px;
    height: 380px;
    box-sizing: border-box;
    padding: 0 34px;
    background: var(--sign-paper);
    border: 14px solid var(--sign-gold);
    border-radius: 26px;
    box-shadow: inset 0 0 0 3px var(--sign-gold-deep), 0 0 0 3px var(--sign-gold-deep);
    display: flex;
    align-items: center;
  }
  .sign-stars {
    position: absolute;
    left: 50%;
    top: -50px;
    transform: translateX(-50%);
  }
  .title {
    margin: 0;
    width: 100%;
    font-family: "Rye", serif;
    font-weight: 400;
    color: var(--plum);
    line-height: 1;
  }
  .title-top {
    display: block;
    font-size: 48px;
    letter-spacing: 1px;
  }
  .title-lower {
    display: flex;
    align-items: flex-end;
    justify-content: space-between;
    margin-top: 26px;
  }
  .title-mid {
    font-size: 48px;
    padding-bottom: 6px;
  }
  .title-gin {
    font-family: "Alfa Slab One", serif;
    font-size: 92px;
    color: var(--rose);
    -webkit-text-stroke: 4px var(--sign-gold);
    paint-order: stroke fill;
    line-height: 0.9;
  }
  .fairground {
    position: absolute;
    left: 140px;
    top: 482px;
    width: 340px;
    height: 250px;
    border-radius: 24px;
    background: linear-gradient(180deg, var(--lilac), var(--orchid));
    opacity: 0.9;
  }
  .age-badge {
    position: absolute;
    left: 506px;
    top: 672px;
    width: 150px;
    height: 84px;
    box-sizing: border-box;
    border: 6px solid var(--ink);
    border-radius: 8px;
    background: rgba(246, 235, 228, 0.7);
    display: flex;
    align-items: center;
    justify-content: center;
    font-family: "Alfa Slab One", serif;
    font-size: 54px;
    color: var(--ink);
    transform: rotate(-4deg);
  }
</style>
</head>
<body>
  <main class="canvas">
    <section class="label">
      <div class="sunburst" role="img" aria-label="Pink and cream vintage sunburst rays radiating from the centre"></div>
      <div class="bunting" role="img" aria-label="Strings of colourful festival bunting flags"></div>

      <div class="sign">
        <svg class="sign-stars" width="160" height="60" viewBox="0 0 160 60" aria-hidden="true">
          <polygon fill="#f0c24f" points="80,2 88,24 112,24 92,38 100,58 80,45 60,58 68,38 48,24 72,24"/>
          <polygon fill="#f0c24f" points="30,18 34,30 46,30 36,37 40,48 30,41 20,48 24,37 14,30 26,30"/>
          <polygon fill="#f0c24f" points="130,18 134,30 146,30 136,37 140,48 130,41 120,48 124,37 114,30 126,30"/>
        </svg>
        <h1 class="title">
          <span class="title-top">LEMON VELVET</span>
          <span class="title-lower">
            <span class="title-mid">MEADOW</span>
            <span class="title-gin">GIN</span>
          </span>
        </h1>
      </div>

      <div class="fairground" role="img" aria-label="Illustration of a striped circus big top with hot air balloons and pinwheels beside it"></div>

      <div class="age-badge">18+</div>
    </section>
  </main>
</body>
</html>
```